"MEET THE TEAM" page web design

We need a "meet the team" page for our website!
Please look at our website to see the style we need

We are looking for something unique, fun, cool, technology-style and yet professional. We plan on taking a picture of each employee (not sure if this will be a real photo/caricature/ black and white/goofy picture--> but we are open to any ideas you have that will work with the design) and putting it there, along with a little bio about each person.

Thanks! looking forward to working together:)
Updates

Project Deadline Extended
Reason: I am excited to see more designs and find the perfect fit. Thanks designers :)

Target Market(s)

People looking to purchase servers, workstations, components

Industry/Entity Type

Information Technology

Number of Pages Required

1 page

Font styles to use
Sans Serif
Other font styles liked:
• The font we use on our site so it matches

Requirements
Must have
• please look at our website qondimex.com and see the theme and colors we want.
• We have 13 employees but would like to have a design where we can add/remove people if we hire/terminate them without messing up the design.
• We are looking for something unique, fun, cool, technology-style and yet professional. We plan on taking a picture of each employee (not sure if this will be a real photo/caricature/ black and white/goofy picture--> but we are open to any ideas you have that will work with the design) and putting it there, along with a little bio about each person.
• We can upload anything you need
Nice to have
• We are also interested in having a design where when the cursor moves over a person then the bio comes out or moves around, or something. (This is not required, but we would love some cool ideas) And if you can come up with some design, we would have our programmers create it for us.
Should not have
• we are open to anything

```html
<!DOCTYPE html>
<html lang="en">
<head>
<meta charset="utf-8">
<title>Meet the Team – Qondimex</title>
<link href="https://fonts.googleapis.com/css2?family=Arimo:wght@400;700&display=swap" rel="stylesheet">
<style>
:root{
  --teal:#2fc2b5;
  --ink:#333;
  --muted:#555;
  --card:#e2e0e0;
  --bar:#535353;
  --footer:#a5a5a5;
  --footer-dark:#999;
  --photo-a:#9a9a9a;
  --photo-b:#5e5e5e;
}
*{box-sizing:border-box;margin:0;padding:0}
html,body{width:925px;height:1200px;overflow:hidden;background:#fff}
body{position:relative;font-family:"Arimo",Arial,sans-serif;color:var(--ink)}
.abs{position:absolute}

/* header */
.account-tab{left:774px;top:0;width:104px;height:18px;background:#9e9e9e;border-radius:0 0 12px 12px;display:flex;font-size:6px;color:#fff}
.account-tab span{flex:1;display:flex;align-items:center;justify-content:center}
.account-tab span+span{background:#8a8a8a;border-radius:0 0 12px 0}
.brand{left:48px;top:14px;display:flex;align-items:center;gap:8px}
.brand-mark{width:28px;height:28px;background:var(--teal)}
.brand-name{font-size:22px;color:var(--teal);letter-spacing:2px;font-weight:400}
.contact-top{top:26px;left:712px;display:flex;align-items:center;font-size:8px;color:var(--muted)}
.round-icon{width:22px;height:22px;border:1px solid #cfd;border-radius:50%;display:flex;align-items:center;justify-content:center}
.contact-top .phone-num{font-size:10.5px;color:var(--ink);margin-left:6px}
.rule-top{left:0;top:54px;width:925px;height:1px;background:#e6e6e6}
.nav{left:54px;top:64px;display:flex;font-size:7.8px;color:#444}
.nav span{margin-right:14.5px}
.search{left:712px;top:61px;width:125px;height:18px;border:1px solid #bbb;border-radius:9px;font-size:6px;color:#555;padding:5px 0 0 15px}
.search svg{position:absolute;right:6px;top:4px}
.cart{left:848px;top:59px;width:20px;height:20px;border:1px solid var(--teal);border-radius:50%;display:flex;align-items:center;justify-content:center}
.crumb-band{left:0;top:82px;width:925px;height:20px;background:linear-gradient(90deg,#2bb6ad,#3fd2c3,#2bb6ad)}
.crumb{left:48px;top:89px;font-size:6.5px;color:#fff;font-weight:700}

/* section title */
.section-title{left:0;top:118px;width:925px;text-align:center;font-size:11.5px;font-weight:400;color:#333;letter-spacing:.3px}
.section-title::after{content:"";display:block;width:28px;height:4px;margin:4px auto 0;border-top:1px solid #888;border-bottom:1px solid #888}

/* team grid */
.team{left:46px;top:160px;width:834px;display:flex;flex-wrap:wrap;justify-content:center;column-gap:17.5px;row-gap:16px}
.member{position:relative;width:152px;height:243px;text-align:center}
.member-panel{position:absolute;left:0;top:50px;width:152px;height:163px;background:var(--card)}
.member-photo{position:absolute;left:11px;top:0}
.member-name{position:absolute;left:0;top:141px;width:152px;font-size:7.5px;font-weight:700;color:#333}
.member-role{position:absolute;left:0;top:153px;width:152px;font-size:7.5px;color:#555}
.member-bio{position:absolute;left:7px;top:169px;width:138px;font-size:6.2px;line-height:8px;color:#555}
.member-links{position:absolute;left:0;top:213px;width:152px;height:30px;background:var(--bar);display:flex;justify-content:center;align-items:center;gap:8px}
.link-box{width:14px;height:14px;background:#fff;display:flex;align-items:center;justify-content:center}
.member.is-active .member-name{color:var(--teal)}
.member.is-active .member-links{background:var(--teal)}
.member.is-active .link-box{background:#e8fbf9}

/* footer */
.footer{left:0;top:947px;width:925px;height:157px;background:var(--footer);color:#fff}
.footer-base{left:0;top:1104px;width:925px;height:96px;background:var(--footer-dark)}
.footer-about{left:272px;top:12px;width:380px;text-align:center;font-size:8px;line-height:10.7px}
.footer-rule{left:240px;top:58px;width:470px;height:1px;background:#b8b8b8}
.footer-contact{top:70px;font-size:8px;line-height:11px;display:flex;gap:6px}
.footer-links{top:107px;font-size:9px}
.footer-sub{left:600px;top:120px;width:90px;text-align:center;font-size:5.2px;line-height:7.7px}
.social{top:1115px;width:21px;height:21px;border:1px solid #ddd;border-radius:50%}
.base-rule{left:240px;top:1146px;width:470px;height:1px;background:#b5b5b5}
.copyright{left:422px;top:1154px;display:flex;gap:6px;align-items:center;color:#fff;font-size:7px;line-height:9px}
.copyright i{display:block;width:12px;height:12px;background:#fff}
.chat-now{left:810px;top:1186px;width:115px;height:14px;background:var(--teal);color:#fff;font-size:7px;font-weight:700;padding:3px 0 0 5px}
</style>
</head>
<body>

<header>
  <div class="abs account-tab"><span>SIGN UP</span><span>LOGIN</span></div>
  <div class="abs brand"><div class="brand-mark"></div><div class="brand-name">QONDIMEX</div></div>
  <div class="abs contact-top">
    <div class="round-icon"><svg width="10" height="9" viewBox="0 0 10 9"><path d="M1 1h8v5H4L2 8V6H1z" fill="var(--teal)"/></svg></div>
    <span style="margin:0 14px 0 5px">LIVE CHAT</span>
    <div class="round-icon"><svg width="10" height="10" viewBox="0 0 10 10"><path d="M2 1l2 2-1 1.5c.6 1.3 1.3 2 2.5 2.5L7 6l2 2-1.5 1.5C4 9 1 6 .5 2.5z" fill="var(--teal)"/></svg></div>
    <span class="phone-num">555-014-2290</span>
  </div>
  <div class="abs rule-top"></div>
  <nav class="abs nav">
    <span>SERVERS</span><span>WORKSTATIONS</span><span>COMPONENTS</span><span>VIRTUAL REALITY</span><span>DRONES</span><span>ABOUT US</span><span>BLOG</span><span>RESOURCES</span><span>CONTACT US</span>
  </nav>
  <div class="abs search">Search<svg width="8" height="8" viewBox="0 0 8 8"><circle cx="3.2" cy="3.2" r="2.4" fill="none" stroke="var(--teal)" stroke-width="1.2"/><path d="M5 5l2.5 2.5" stroke="var(--teal)" stroke-width="1.2"/></svg></div>
  <div class="abs cart"><svg width="10" height="9" viewBox="0 0 10 9"><path d="M0 1h2l1 5h6l1-4H3" fill="none" stroke="var(--teal)" stroke-width="1.2"/><circle cx="4" cy="8" r="1" fill="var(--teal)"/><circle cx="8" cy="8" r="1" fill="var(--teal)"/></svg></div>
  <div class="abs crumb-band"></div>
  <div class="abs crumb">HOME / MEET THE TEAM</div>
</header>

<h1 class="abs section-title">MEET THE TEAM</h1>

<svg width="0" height="0" style="position:absolute"><defs><linearGradient id="pg" x1="0" y1="0" x2="0" y2="1"><stop offset="0" stop-color="#9a9a9a"/><stop offset="1" stop-color="#5e5e5e"/></linearGradient></defs></svg>

<main class="abs team">
  <article class="member">
    <div class="member-panel"></div>
    <svg class="member-photo" width="130" height="128" viewBox="0 0 130 128" role="img" aria-label="Employee portrait photo"><polygon points="1,1 129,1 129,101 65,127 1,101" fill="url(#pg)" stroke="#4a4a4a" stroke-width="1.5"/></svg>
    <div class="member-name">Name of Employee</div><div class="member-role">Business Analyst</div>
    <p class="member-bio">Aliquam et suscipit odio. Cras maximus, quam et convallis mattis, urna sem luctus leo, quis vulputate lorem nisl congue libero. Nullam eget lectus sapien.</p>
    <div class="member-links"><span class="link-box"><svg width="8" height="8" viewBox="0 0 10 10"><path d="M2 1l2 2-1 1.5c.6 1.3 1.3 2 2.5 2.5L7 6l2 2-1.5 1.5C4 9 1 6 .5 2.5z" fill="#444"/></svg></span><span class="link-box"><svg width="8" height="6" viewBox="0 0 8 6"><rect width="8" height="6" fill="#444"/><path d="M0 0l4 3 4-3" stroke="#fff" fill="none" stroke-width=".8"/></svg></span><span class="link-box"></span><span class="link-box"></span></div>
  </article>
  <article class="member">
    <div class="member-panel"></div>
    <svg class="member-photo" width="130" height="128" viewBox="0 0 130 128" role="img" aria-label="Employee portrait photo"><polygon points="1,1 129,1 129,101 65,127 1,101" fill="url(#pg)" stroke="#4a4a4a" stroke-width="1.5"/></svg>
    <div class="member-name">Name of Employee</div><div class="member-role">Business Analyst</div>
    <p class="member-bio">Aliquam et suscipit odio. Cras maximus, quam et convallis mattis, urna sem luctus leo, quis vulputate lorem nisl congue libero. Nullam eget lectus sapien.</p>
    <div class="member-links"><span class="link-box"><svg width="8" height="8" viewBox="0 0 10 10"><path d="M2 1l2 2-1 1.5c.6 1.3 1.3 2 2.5 2.5L7 6l2 2-1.5 1.5C4 9 1 6 .5 2.5z" fill="#444"/></svg></span><span class="link-box"><svg width="8" height="6" viewBox="0 0 8 6"><rect width="8" height="6" fill="#444"/><path d="M0 0l4 3 4-3" stroke="#fff" fill="none" stroke-width=".8"/></svg></span><span class="link-box"></span><span class="link-box"></span></div>
  </article>
  <article class="member is-active">
    <div class="member-panel"></div>
    <svg class="member-photo" width="130" height="128" viewBox="0 0 130 128" role="img" aria-label="Employee portrait photo"><polygon points="1,1 129,1 129,101 65,127 1,101" fill="url(#pg)" stroke="var(--teal)" stroke-width="1.5"/></svg>
    <div class="member-name">Name of Employee</div><div class="member-role">Business Analyst</div>
    <p class="member-bio">Aliquam et suscipit odio. Cras maximus, quam et convallis mattis, urna sem luctus leo, quis vulputate lorem nisl congue libero. Nullam eget lectus sapien.</p>
    <div class="member-links"><span class="link-box"><svg width="8" height="8" viewBox="0 0 10 10"><path d="M2 1l2 2-1 1.5c.6 1.3 1.3 2 2.5 2.5L7 6l2 2-1.5 1.5C4 9 1 6 .5 2.5z" fill="var(--teal)"/></svg></span><span class="link-box"><svg width="8" height="6" viewBox="0 0 8 6"><rect width="8" height="6" fill="var(--teal)"/><path d="M0 0l4 3 4-3" stroke="#fff" fill="none" stroke-width=".8"/></svg></span><span class="link-box"></span><span class="link-box"></span></div>
  </article>
  <article class="member">
    <div class="member-panel"></div>
    <svg class="member-photo" width="130" height="128" viewBox="0 0 130 128" role="img" aria-label="Employee portrait photo"><polygon points="1,1 129,1 129,101 65,127 1,101" fill="url(#pg)" stroke="#4a4a4a" stroke-width="1.5"/></svg>
    <div class="member-name">Name of Employee</div><div class="member-role">Business Analyst</div>
    <p class="member-bio">Aliquam et suscipit odio. Cras maximus, quam et convallis mattis, urna sem luctus leo, quis vulputate lorem nisl congue libero. Nullam eget lectus sapien.</p>
    <div class="member-links"><span class="link-box"><svg width="8" height="8" viewBox="0 0 10 10"><path d="M2 1l2 2-1 1.5c.6 1.3 1.3 2 2.5 2.5L7 6l2 2-1.5 1.5C4 9 1 6 .5 2.5z" fill="#444"/></svg></span><span class="link-box"><svg width="8" height="6" viewBox="0 0 8 6"><rect width="8" height="6" fill="#444"/><path d="M0 0l4 3 4-3" stroke="#fff" fill="none" stroke-width=".8"/></svg></span><span class="link-box"></span><span class="link-box"></span></div>
  </article>
  <article class="member">
    <div class="member-panel"></div>
    <svg class="member-photo" width="130" height="128" viewBox="0 0 130 128" role="img" aria-label="Employee portrait photo"><polygon points="1,1 129,1 129,101 65,127 1,101" fill="url(#pg)" stroke="#4a4a4a" stroke-width="1.5"/></svg>
    <div class="member-name">Name of Employee</div><div class="member-role">Business Analyst</div>
    <p class="member-bio">Aliquam et suscipit odio. Cras maximus, quam et convallis mattis, urna sem luctus leo, quis vulputate lorem nisl congue libero. Nullam eget lectus sapien.</p>
    <div class="member-links"><span class="link-box"><svg width="8" height="8" viewBox="0 0 10 10"><path d="M2 1l2 2-1 1.5c.6 1.3 1.3 2 2.5 2.5L7 6l2 2-1.5 1.5C4 9 1 6 .5 2.5z" fill="#444"/></svg></span><span class="link-box"><svg width="8" height="6" viewBox="0 0 8 6"><rect width="8" height="6" fill="#444"/><path d="M0 0l4 3 4-3" stroke="#fff" fill="none" stroke-width=".8"/></svg></span><span class="link-box"></span><span class="link-box"></span></div>
  </article>
  <article class="member">
    <div class="member-panel"></div>
    <svg class="member-photo" width="130" height="128" viewBox="0 0 130 128" role="img" aria-label="Employee portrait photo"><polygon points="1,1 129,1 129,101 65,127 1,101" fill="url(#pg)" stroke="#4a4a4a" stroke-width="1.5"/></svg>
    <div class="member-name">Name of Employee</div><div class="member-role">Business Analyst</div>
    <p class="member-bio">Aliquam et suscipit odio. Cras maximus, quam et convallis mattis, urna sem luctus leo, quis vulputate lorem nisl congue libero. Nullam eget lectus sapien.</p>
    <div class="member-links"><span class="link-box"><svg width="8" height="8" viewBox="0 0 10 10"><path d="M2 1l2 2-1 1.5c.6 1.3 1.3 2 2.5 2.5L7 6l2 2-1.5 1.5C4 9 1 6 .5 2.5z" fill="#444"/></svg></span><span class="link-box"><svg width="8" height="6" viewBox="0 0 8 6"><rect width="8" height="6" fill="#444"/><path d="M0 0l4 3 4-3" stroke="#fff" fill="none" stroke-width=".8"/></svg></span><span class="link-box"></span><span class="link-box"></span></div>
  </article>
  <article class="member">
    <div class="member-panel"></div>
    <svg class="member-photo" width="130" height="128" viewBox="0 0 130 128" role="img" aria-label="Employee portrait photo"><polygon points="1,1 129,1 129,101 65,127 1,101" fill="url(#pg)" stroke="#4a4a4a" stroke-width="1.5"/></svg>
    <div class="member-name">Name of Employee</div><div class="member-role">Business Analyst</div>
    <p class="member-bio">Aliquam et suscipit odio. Cras maximus, quam et convallis mattis, urna sem luctus leo, quis vulputate lorem nisl congue libero. Nullam eget lectus sapien.</p>
    <div class="member-links"><span class="link-box"><svg width="8" height="8" viewBox="0 0 10 10"><path d="M2 1l2 2-1 1.5c.6 1.3 1.3 2 2.5 2.5L7 6l2 2-1.5 1.5C4 9 1 6 .5 2.5z" fill="#444"/></svg></span><span class="link-box"><svg width="8" height="6" viewBox="0 0 8 6"><rect width="8" height="6" fill="#444"/><path d="M0 0l4 3 4-3" stroke="#fff" fill="none" stroke-width=".8"/></svg></span><span class="link-box"></span><span class="link-box"></span></div>
  </article>
  <article class="member">
    <div class="member-panel"></div>
    <svg class="member-photo" width="130" height="128" viewBox="0 0 130 128" role="img" aria-label="Employee portrait photo"><polygon points="1,1 129,1 129,101 65,127 1,101" fill="url(#pg)" stroke="#4a4a4a" stroke-width="1.5"/></svg>
    <div class="member-name">Name of Employee</div><div class="member-role">Business Analyst</div>
    <p class="member-bio">Aliquam et suscipit odio. Cras maximus, quam et convallis mattis, urna sem luctus leo, quis vulputate lorem nisl congue libero. Nullam eget lectus sapien.</p>
    <div class="member-links"><span class="link-box"><svg width="8" height="8" viewBox="0 0 10 10"><path d="M2 1l2 2-1 1.5c.6 1.3 1.3 2 2.5 2.5L7 6l2 2-1.5 1.5C4 9 1 6 .5 2.5z" fill="#444"/></svg></span><span class="link-box"><svg width="8" height="6" viewBox="0 0 8 6"><rect width="8" height="6" fill="#444"/><path d="M0 0l4 3 4-3" stroke="#fff" fill="none" stroke-width=".8"/></svg></span><span class="link-box"></span><span class="link-box"></span></div>
  </article>
  <article class="member">
    <div class="member-panel"></div>
    <svg class="member-photo" width="130" height="128" viewBox="0 0 130 128" role="img" aria-label="Employee portrait photo"><polygon points="1,1 129,1 129,101 65,127 1,101" fill="url(#pg)" stroke="#4a4a4a" stroke-width="1.5"/></svg>
    <div class="member-name">Name of Employee</div><div class="member-role">Business Analyst</div>
    <p class="member-bio">Aliquam et suscipit odio. Cras maximus, quam et convallis mattis, urna sem luctus leo, quis vulputate lorem nisl congue libero. Nullam eget lectus sapien.</p>
    <div class="member-links"><span class="link-box"><svg width="8" height="8" viewBox="0 0 10 10"><path d="M2 1l2 2-1 1.5c.6 1.3 1.3 2 2.5 2.5L7 6l2 2-1.5 1.5C4 9 1 6 .5 2.5z" fill="#444"/></svg></span><span class="link-box"><svg width="8" height="6" viewBox="0 0 8 6"><rect width="8" height="6" fill="#444"/><path d="M0 0l4 3 4-3" stroke="#fff" fill="none" stroke-width=".8"/></svg></span><span class="link-box"></span><span class="link-box"></span></div>
  </article>
  <article class="member">
    <div class="member-panel"></div>
    <svg class="member-photo" width="130" height="128" viewBox="0 0 130 128" role="img" aria-label="Employee portrait photo"><polygon points="1,1 129,1 129,101 65,127 1,101" fill="url(#pg)" stroke="#4a4a4a" stroke-width="1.5"/></svg>
    <div class="member-name">Name of Employee</div><div class="member-role">Business Analyst</div>
    <p class="member-bio">Aliquam et suscipit odio. Cras maximus, quam et convallis mattis, urna sem luctus leo, quis vulputate lorem nisl congue libero. Nullam eget lectus sapien.</p>
    <div class="member-links"><span class="link-box"><svg width="8" height="8" viewBox="0 0 10 10"><path d="M2 1l2 2-1 1.5c.6 1.3 1.3 2 2.5 2.5L7 6l2 2-1.5 1.5C4 9 1 6 .5 2.5z" fill="#444"/></svg></span><span class="link-box"><svg width="8" height="6" viewBox="0 0 8 6"><rect width="8" height="6" fill="#444"/><path d="M0 0l4 3 4-3" stroke="#fff" fill="none" stroke-width=".8"/></svg></span><span class="link-box"></span><span class="link-box"></span></div>
  </article>
  <article class="member">
    <div class="member-panel"></div>
    <svg class="member-photo" width="130" height="128" viewBox="0 0 130 128" role="img" aria-label="Employee portrait photo"><polygon points="1,1 129,1 129,101 65,127 1,101" fill="url(#pg)" stroke="#4a4a4a" stroke-width="1.5"/></svg>
    <div class="member-name">Name of Employee</div><div class="member-role">Business Analyst</div>
    <p class="member-bio">Aliquam et suscipit odio. Cras maximus, quam et convallis mattis, urna sem luctus leo, quis vulputate lorem nisl congue libero. Nullam eget lectus sapien.</p>
    <div class="member-links"><span class="link-box"><svg width="8" height="8" viewBox="0 0 10 10"><path d="M2 1l2 2-1 1.5c.6 1.3 1.3 2 2.5 2.5L7 6l2 2-1.5 1.5C4 9 1 6 .5 2.5z" fill="#444"/></svg></span><span class="link-box"><svg width="8" height="6" viewBox="0 0 8 6"><rect width="8" height="6" fill="#444"/><path d="M0 0l4 3 4-3" stroke="#fff" fill="none" stroke-width=".8"/></svg></span><span class="link-box"></span><span class="link-box"></span></div>
  </article>
  <article class="member">
    <div class="member-panel"></div>
    <svg class="member-photo" width="130" height="128" viewBox="0 0 130 128" role="img" aria-label="Employee portrait photo"><polygon points="1,1 129,1 129,101 65,127 1,101" fill="url(#pg)" stroke="#4a4a4a" stroke-width="1.5"/></svg>
    <div class="member-name">Name of Employee</div><div class="member-role">Business Analyst</div>
    <p class="member-bio">Aliquam et suscipit odio. Cras maximus, quam et convallis mattis, urna sem luctus leo, quis vulputate lorem nisl congue libero. Nullam eget lectus sapien.</p>
    <div class="member-links"><span class="link-box"><svg width="8" height="8" viewBox="0 0 10 10"><path d="M2 1l2 2-1 1.5c.6 1.3 1.3 2 2.5 2.5L7 6l2 2-1.5 1.5C4 9 1 6 .5 2.5z" fill="#444"/></svg></span><span class="link-box"><svg width="8" height="6" viewBox="0 0 8 6"><rect width="8" height="6" fill="#444"/><path d="M0 0l4 3 4-3" stroke="#fff" fill="none" stroke-width=".8"/></svg></span><span class="link-box"></span><span class="link-box"></span></div>
  </article>
  <article class="member">
    <div class="member-panel"></div>
    <svg class="member-photo" width="130" height="128" viewBox="0 0 130 128" role="img" aria-label="Employee portrait photo"><polygon points="1,1 129,1 129,101 65,127 1,101" fill="url(#pg)" stroke="#4a4a4a" stroke-width="1.5"/></svg>
    <div class="member-name">Name of Employee</div><div class="member-role">Business Analyst</div>
    <p class="member-bio">Aliquam et suscipit odio. Cras maximus, quam et convallis mattis, urna sem luctus leo, quis vulputate lorem nisl congue libero. Nullam eget lectus sapien.</p>
    <div class="member-links"><span class="link-box"><svg width="8" height="8" viewBox="0 0 10 10"><path d="M2 1l2 2-1 1.5c.6 1.3 1.3 2 2.5 2.5L7 6l2 2-1.5 1.5C4 9 1 6 .5 2.5z" fill="#444"/></svg></span><span class="link-box"><svg width="8" height="6" viewBox="0 0 8 6"><rect width="8" height="6" fill="#444"/><path d="M0 0l4 3 4-3" stroke="#fff" fill="none" stroke-width=".8"/></svg></span><span class="link-box"></span><span class="link-box"></span></div>
  </article>
</main>

<footer>
  <div class="abs footer">
    <p class="abs footer-about">Based in Brellmont California, Qondimex offers custom servers, storage, and workstations for local businesses in Los Angeles, Beverly Hills, Thousand Oaks, Ventura, Orange County, Santa Barbara, Oxnard, Irvine, Anaheim, and San Diego. Qondimex also offers such products to clients throughout the United States and Worldwide.</p>
    <div class="abs footer-rule"></div>
    <div class="abs footer-contact" style="left:290px"><svg width="7" height="9" viewBox="0 0 7 9"><path d="M3.5 0A3.2 3.2 0 0 0 .3 3.2C.3 5.5 3.5 9 3.5 9s3.2-3.5 3.2-5.8A3.2 3.2 0 0 0 3.5 0z" fill="#fff"/><circle cx="3.5" cy="3.2" r="1.2" fill="var(--footer)"/></svg><span>4820 Larkmoor Ave.<br>Brellmont, CA 90000</span></div>
    <div class="abs footer-contact" style="left:434px"><svg width="8" height="8" viewBox="0 0 10 10"><path d="M2 1l2 2-1 1.5c.6 1.3 1.3 2 2.5 2.5L7 6l2 2-1.5 1.5C4 9 1 6 .5 2.5z" fill="#fff"/></svg><span>555-014-2290</span></div>
    <div class="abs footer-contact" style="left:559px"><svg width="8" height="7" viewBox="0 0 8 6" style="margin-top:2px"><rect width="8" height="6" fill="#fff"/><path d="M0 0l4 3 4-3" stroke="var(--footer)" fill="none" stroke-width=".8"/></svg><span>sales@qondimex.com</span></div>
    <div class="abs footer-links" style="left:241px">Computer Hardware</div>
    <div class="abs footer-links" style="left:365px">Drones</div>
    <div class="abs footer-links" style="left:426px">Virtual Reality</div>
    <div class="abs footer-links" style="left:520px">About Us</div>
    <div class="abs footer-links" style="left:606px">Customer Support</div>
    <div class="abs footer-sub">Terms and Conditions<br>Warranty Information<br>Contact Us<br>Return Policy</div>
  </div>
  <div class="abs footer-base"></div>
  <div class="abs social" style="left:403px" aria-label="Social profile"></div>
  <div class="abs social" style="left:432px" aria-label="Social profile"></div>
  <div class="abs social" style="left:461px" aria-label="Social profile"></div>
  <div class="abs social" style="left:490px" aria-label="Social profile"></div>
  <div class="abs base-rule"></div>
  <div class="abs copyright"><i></i><span>Qondimex, LLC.<br>Copyright © 2017</span></div>
  <div class="abs chat-now">CHAT NOW</div>
</footer>

</body>
</html>
```